New Web Design Project

New Roofing Website homepage mockup

Complete design document here: https://files.plorvex.net/doc/7tQmZrA2kLwP9xVbN4cYhE3sJdF8gUoR6iKe1nTy/edit?usp=sharing
Updates

Number of Pages Required

1 page

Font styles to use
Sans Serif

```html
<!DOCTYPE html>
<html lang="en">
<head>
<meta charset="utf-8">
<title>Everstead Roofing</title>
<link href="https://fonts.googleapis.com/css2?family=Montserrat:wght@400;500;600;700&family=Open+Sans:wght@400;600&display=swap" rel="stylesheet">
<style>
:root{
  --blue:#2aa4e2;
  --blue-dark:#1b87c2;
  --ink:#2d3138;
  --text:#6a6f76;
  --muted:#9aa0a6;
  --line:#e3e6ea;
  --white:#ffffff;
  --band-gray:#55595f;
  --footer:#26292d;
  --footer-bar:#1e2024;
}
*{box-sizing:border-box;margin:0;padding:0}
html,body{width:1200px;height:4500px;overflow:hidden}
body{font-family:"Open Sans",Arial,sans-serif;color:var(--text);background:var(--white);position:relative}
h1,h2,h3,.nav,.btn,.label{font-family:"Montserrat",Arial,sans-serif}

/* header */
.site-header{height:72px;display:flex;align-items:center;padding:0 60px;background:var(--white);position:relative;z-index:3}
.brand{display:flex;align-items:center;gap:10px;font-family:"Montserrat",sans-serif;font-weight:700;font-size:20px;color:var(--blue-dark);letter-spacing:.5px}
.brand-mark{width:14px;height:14px;background:var(--blue)}
.nav{display:flex;gap:34px;margin-left:auto;margin-right:40px;font-size:11px;font-weight:600;color:var(--ink);letter-spacing:.6px}
.nav a{color:inherit;text-decoration:none}
.nav .active{color:var(--blue);border-bottom:2px solid var(--blue);padding-bottom:4px}
.header-contact{display:flex;align-items:center;gap:8px;font-size:13px;font-weight:600;color:var(--blue)}
.header-contact .call{margin-right:10px}
.social-dot{width:26px;height:26px;border-radius:50%;border:1.5px solid var(--blue)}
.social-dot.filled{background:var(--blue)}

/* hero */
.hero{height:580px;position:relative;background:linear-gradient(180deg,#8fa2b2 0%,#6f7d86 45%,#4f5a55 100%)}
.hero-photo{position:absolute;inset:0;background:linear-gradient(180deg,rgba(150,170,190,.6),rgba(70,78,72,.8))}
.hero-content{position:absolute;top:235px;left:0;right:0;text-align:center}
.hero h1{color:var(--white);font-size:50px;font-weight:600;letter-spacing:1px}
.btn{display:inline-block;font-size:10px;font-weight:600;letter-spacing:1px;padding:9px 24px;border-radius:20px;text-transform:uppercase}
.btn-ghost-light{border:1.5px solid var(--white);color:var(--white);margin-top:28px}
.btn-outline{border:1.5px solid var(--blue);color:var(--blue)}

/* services */
.services{height:488px;position:relative}
.feature-row{position:absolute;top:-30px;left:0;right:0;display:flex;justify-content:center;gap:64px}
.feature-card{width:310px;height:258px;background:var(--white);box-shadow:0 6px 18px rgba(0,0,0,.12);position:relative}
.feature-card .photo{height:200px}
.feature-card .label{position:absolute;left:16px;bottom:24px;font-size:15px;font-weight:600;color:var(--ink);padding:10px 16px;background:var(--white)}
.feature-card.primary .label{background:var(--blue);color:var(--white);width:250px}
.install-photo{background:linear-gradient(135deg,#7d8a95,#c9b76a 60%,#6d6f72)}
.repair-photo{background:linear-gradient(135deg,#e9eef2,#8f9aa3 55%,#b7c2a0)}
.mini-row{position:absolute;top:268px;left:88px;right:88px;display:flex;gap:20px}
.mini-card{flex:1;height:180px;box-shadow:0 4px 12px rgba(0,0,0,.1);background:var(--white)}
.mini-card .photo{height:140px}
.mini-card .label{text-align:center;font-size:12px;font-weight:500;color:var(--ink);padding-top:12px}
.p-windows{background:linear-gradient(135deg,#6e8399,#c9d3db)}
.p-gutters{background:linear-gradient(135deg,#c2c6c4,#7c8386)}
.p-siding{background:linear-gradient(135deg,#d9dcdd,#9ea6aa)}
.p-interior{background:linear-gradient(135deg,#e3e4e2,#b9b6b0)}

/* about */
.about{height:340px;text-align:center;padding-top:60px}
.section-title{font-size:26px;font-weight:600;color:var(--blue);letter-spacing:1px;text-transform:uppercase}
.section-title::after{content:"";display:block;width:60px;height:2px;background:var(--blue);margin:12px auto 0}
.about p{width:760px;margin:26px auto 30px;font-size:12px;line-height:1.8}

/* types */
.types{height:400px;background:var(--blue);text-align:center;padding-top:80px}
.types .section-title{color:var(--white)}
.types .section-title::after{background:var(--white)}
.roof-tiles{display:flex;gap:16px;justify-content:center;margin-top:40px}
.roof-tile{width:196px;height:190px;background:var(--white);padding:6px}
.roof-tile .swatch{height:148px}
.roof-tile .label{font-size:11px;font-weight:600;color:var(--ink);padding-top:10px;letter-spacing:.8px}
.s-cedar{background:linear-gradient(135deg,#c99a6b,#a87449)}
.s-metal{background:linear-gradient(135deg,#9aa1a6,#5f666b)}
.s-slate{background:linear-gradient(135deg,#5a5e62,#33363a)}
.s-asphalt{background:linear-gradient(135deg,#6b6d70,#45474a)}
.s-rubber{background:linear-gradient(135deg,#a9c3cf,#6f8e9c)}

/* projects */
.projects{height:960px;text-align:center;padding-top:160px}
.project-grid{width:760px;margin:40px auto 0;display:grid;grid-template-columns:repeat(3,1fr);gap:12px}
.project{height:278px;position:relative}
.project.featured{background:linear-gradient(180deg,#3b3f44,#25282c)}
.project.featured .label{position:absolute;top:118px;left:0;right:0;color:var(--white);font-size:22px;font-weight:500}
.pr2{background:linear-gradient(180deg,#a9c0d6,#8b9a86)}
.pr3{background:linear-gradient(180deg,#7fb0e0,#d9dde0)}
.pr4{background:linear-gradient(180deg,#b6b2a8,#6c6860)}
.pr5{background:linear-gradient(180deg,#9bb7d6,#3d4145)}
.pr6{background:linear-gradient(180deg,#e7ecef,#6f8d5a)}
.projects .btn{margin-top:50px}

/* calculator */
.calculator{height:680px;background:var(--band-gray);text-align:center;padding-top:100px}
.calculator .section-title{color:var(--white)}
.calculator .section-title::after{background:var(--white)}
.steps{display:flex;justify-content:center;margin-top:36px}
.step{width:265px;height:36px;line-height:36px;font-size:11px;font-weight:600;color:var(--white);background:#6c7076;clip-path:polygon(0 0,92% 0,100% 50%,92% 100%,0 100%,8% 50%);margin-left:-12px}
.step:first-child{clip-path:polygon(0 0,92% 0,100% 50%,92% 100%,0 100%);margin-left:0;background:var(--blue)}
.calc-cards{display:flex;gap:12px;justify-content:center;margin-top:24px}
.calc-card{width:196px;height:346px;background:var(--white);padding:0 0 16px}
.calc-card .swatch{height:160px}
.calc-card .label{font-size:10px;font-weight:600;color:var(--blue);letter-spacing:.8px;padding-top:14px}
.calc-card .product{font-family:"Montserrat",sans-serif;font-size:16px;font-weight:500;color:var(--ink);margin-top:10px;line-height:1.3}
.calc-card .price{font-size:10px;color:var(--muted);margin-top:12px}
.calc-card .btn{margin-top:14px;font-size:8px;padding:6px 14px;border:1px solid var(--blue);color:var(--blue)}
.calc-card .btn.selected{background:var(--blue);color:var(--white)}

/* clients */
.clients{height:620px;text-align:center;padding-top:110px;position:relative}
.avatar{width:80px;height:80px;border-radius:50%;margin:36px auto 0;background:linear-gradient(180deg,#c9ced3,#7b838b)}
.quote{width:640px;margin:28px auto 0;font-size:12px;line-height:1.8;font-style:italic}
.client-name{margin-top:22px;font-size:12px;font-weight:600;color:var(--ink)}
.client-name span{font-weight:400;color:var(--muted)}
.stars{margin-top:8px;display:flex;justify-content:center;gap:3px}
.clients .btn{margin-top:26px}
.slider-arrow{position:absolute;top:300px}
.slider-arrow.left{left:90px}.slider-arrow.right{right:90px}

/* footer */
.site-footer{height:360px;background:var(--footer);color:#c7cbd0;position:relative}
.footer-cols{display:flex;padding:70px 88px 0;gap:0}
.footer-col h3{font-size:13px;font-weight:600;color:var(--white);letter-spacing:.5px;margin-bottom:16px}
.contact-col{width:330px;font-size:11px;line-height:1.9}
.contact-col .phone{color:var(--blue);font-weight:600;font-size:14px}
.contact-col .biz{color:var(--white);font-weight:600;margin-top:10px}
.contact-col .socials{display:flex;gap:8px;margin-top:16px}
.contact-col .socials .social-dot{border-color:#8a9096}
.links-col{width:240px;font-size:11px;line-height:2.1}
.map{width:455px;height:220px;margin-left:auto;background:linear-gradient(135deg,#dfe6da,#c9d5de);position:relative}
.map svg{position:absolute;left:215px;top:80px}
.footer-bar{position:absolute;left:0;right:0;bottom:0;height:70px;border-top:1px solid #3a3e43;display:flex;align-items:center;padding:0 88px;font-size:11px;color:#9ca2a8}
.footer-bar .legal{margin-left:auto;display:flex;gap:36px;margin-right:100px}
.footer-bar .to-top{color:var(--blue)}
</style>
</head>
<body>

<header class="site-header">
  <div class="brand"><span class="brand-mark"></span>EVERSTEAD ROOFING</div>
  <nav class="nav">
    <a class="active">HOME</a><a>SERVICES</a><a>ABOUT US</a><a>TYPES OF ROOFS</a><a>PROJECTS</a><a>HAPPY CLIENTS</a><a>CONTACT US</a>
  </nav>
  <div class="header-contact">
    <span class="call">Call Us
      <svg width="12" height="12" viewBox="0 0 24 24" fill="#2aa4e2"><path d="M6.6 10.8a15.1 15.1 0 0 0 6.6 6.6l2.2-2.2a1 1 0 0 1 1-.25 11.4 11.4 0 0 0 3.6.57 1 1 0 0 1 1 1V20a1 1 0 0 1-1 1A17 17 0 0 1 3 4a1 1 0 0 1 1-1h3.5a1 1 0 0 1 1 1c0 1.25.2 2.45.57 3.57a1 1 0 0 1-.25 1z"/></svg>
      555-014-2381</span>
    <span class="social-dot"></span><span class="social-dot filled"></span><span class="social-dot"></span>
  </div>
</header>

<section class="hero">
  <div class="hero-photo" role="img" aria-label="Large two-storey house with a new grey shingle roof"></div>
  <div class="hero-content">
    <h1>BUILT RIGHT, BUILT TO LAST</h1>
    <span class="btn btn-ghost-light">Get an instant estimate</span>
  </div>
</section>

<section class="services">
  <div class="feature-row">
    <div class="feature-card primary">
      <div class="photo install-photo" role="img" aria-label="Roofer installing shingles"></div>
      <div class="label">ROOF INSTALLATION</div>
    </div>
    <div class="feature-card">
      <div class="photo repair-photo" role="img" aria-label="Roofer repairing a roof"></div>
      <div class="label">ROOF REPAIR</div>
    </div>
  </div>
  <div class="mini-row">
    <div class="mini-card"><div class="photo p-windows" role="img" aria-label="Roof skylight window"></div><div class="label">Windows/Skylights</div></div>
    <div class="mini-card"><div class="photo p-gutters" role="img" aria-label="House gutters"></div><div class="label">Gutters</div></div>
    <div class="mini-card"><div class="photo p-siding" role="img" aria-label="House siding"></div><div class="label">Siding</div></div>
    <div class="mini-card"><div class="photo p-interior" role="img" aria-label="Repaired interior ceiling"></div><div class="label">Interior Damage Repairs</div></div>
  </div>
</section>

<section class="about">
  <h2 class="section-title">Everstead Roofing</h2>
  <p>After over a decade of general contracting, we narrowed our focus to roofing and the most important parts of every home. Homeowners kept coming back with roof, gutter and siding issues, so we built a team that handles them all with care. Protecting the house you love is what we do best.</p>
  <span class="btn btn-outline">About us</span>
</section>

<section class="types">
  <h2 class="section-title">Types of Roofs</h2>
  <div class="roof-tiles">
    <div class="roof-tile"><div class="swatch s-cedar" role="img" aria-label="Cedar shake roof texture"></div><div class="label">CEDAR</div></div>
    <div class="roof-tile"><div class="swatch s-metal" role="img" aria-label="Metal roof texture"></div><div class="label">METAL</div></div>
    <div class="roof-tile"><div class="swatch s-slate" role="img" aria-label="Slate roof texture"></div><div class="label">SLATE</div></div>
    <div class="roof-tile"><div class="swatch s-asphalt" role="img" aria-label="Asphalt shingle texture"></div><div class="label">ASPHALT</div></div>
    <div class="roof-tile"><div class="swatch s-rubber" role="img" aria-label="Rubber roof texture"></div><div class="label">RUBBER</div></div>
  </div>
</section>

<section class="projects">
  <h2 class="section-title">Recent Projects</h2>
  <div class="project-grid">
    <div class="project featured" role="img" aria-label="Lexington project roof"><div class="label">Lexington</div></div>
    <div class="project pr2" role="img" aria-label="Large colonial home roof"></div>
    <div class="project pr3" role="img" aria-label="Cupola with weathervane"></div>
    <div class="project pr4" role="img" aria-label="Arched window and roof detail"></div>
    <div class="project pr5" role="img" aria-label="House with truck in driveway"></div>
    <div class="project pr6" role="img" aria-label="White home with new roof"></div>
  </div>
  <span class="btn btn-outline">View all</span>
</section>

<section class="calculator">
  <h2 class="section-title">Roofing Cost Calculator</h2>
  <div class="steps">
    <div class="step">01 - Choose Your Roof Type</div>
    <div class="step">02 - About Your Roof</div>
    <div class="step">03 - Roof Condition</div>
    <div class="step">04 - Get Your Cost</div>
  </div>
  <div class="calc-cards">
    <div class="calc-card"><div class="swatch s-cedar" role="img" aria-label="Cedar roof sample"></div><div class="label">CEDAR</div><div class="product">Crestline<br>Shingle HD</div><div class="price">$6.80 / SQ FT</div><span class="btn">Choose this type</span></div>
    <div class="calc-card"><div class="swatch s-metal" role="img" aria-label="Metal roof sample"></div><div class="label">METAL</div><div class="product">Crestline<br>Shingle HD</div><div class="price">$7.40 / SQ FT</div><span class="btn">Choose this type</span></div>
    <div class="calc-card"><div class="swatch s-slate" role="img" aria-label="Slate roof sample"></div><div class="label">SLATE</div><div class="product">Crestline<br>Shingle HD</div><div class="price">$9.20 / SQ FT</div><span class="btn selected">Choose this type</span></div>
    <div class="calc-card"><div class="swatch s-asphalt" role="img" aria-label="Asphalt roof sample"></div><div class="label">ASPHALT</div><div class="product">Crestline<br>Shingle HD</div><div class="price">$4.50 / SQ FT</div><span class="btn">Choose this type</span></div>
    <div class="calc-card"><div class="swatch s-rubber" role="img" aria-label="Rubber roof sample"></div><div class="label">RUBBER</div><div class="product">Crestline<br>Shingle HD</div><div class="price">$5.10 / SQ FT</div><span class="btn">Choose this type</span></div>
  </div>
</section>

<section class="clients">
  <h2 class="section-title">Happy Clients</h2>
  <div class="avatar" role="img" aria-label="Client portrait"></div>
  <p class="quote">“The crew showed up on time, explained every step and left the yard cleaner than they found it. Our old roof leaked for years, and now it looks brand new. The price was fair and the quality is outstanding. We would gladly recommend them to any neighbour.”</p>
  <div class="client-name">Dana Whitfield <span>- Happy Customer</span></div>
  <div class="stars">
    <svg width="60" height="12" viewBox="0 0 60 12" fill="#2aa4e2"><g id="st"><path d="M6 0l1.8 3.9 4.2.4-3.2 2.8 1 4.1L6 9.1 2.2 11.2l1-4.1L0 4.3l4.2-.4z"/></g><use href="#st" x="12"/><use href="#st" x="24"/><use href="#st" x="36"/><use href="#st" x="48" fill="#c9ced3"/></svg>
  </div>
  <span class="btn btn-outline">View all</span>
  <svg class="slider-arrow left" width="14" height="24" viewBox="0 0 14 24"><path d="M12 2L2 12l10 10" fill="none" stroke="#b5bac0" stroke-width="2"/></svg>
  <svg class="slider-arrow right" width="14" height="24" viewBox="0 0 14 24"><path d="M2 2l10 10L2 22" fill="none" stroke="#b5bac0" stroke-width="2"/></svg>
</section>

<footer class="site-footer">
  <div class="footer-cols">
    <div class="footer-col contact-col">
      <h3>CONTACT US</h3>
      <div class="phone">Call Us: 555-014-2381</div>
      <div>hello@everstead-roofing.example</div>
      <div class="biz">Everstead Roofing</div>
      <div>12 Harbor Lane, Milford, MA 01757</div>
      <div class="socials"><span class="social-dot"></span><span class="social-dot filled"></span><span class="social-dot"></span></div>
    </div>
    <div class="footer-col links-col">
      <h3>QUICK LINKS</h3>
      <div>Home</div><div>Services</div><div>About Us</div><div>Types Of Roofs</div><div>Recent Projects</div><div>Happy Clients</div><div>Contact Us</div>
    </div>
    <div class="map" role="img" aria-label="Street map showing the office location">
      <svg width="22" height="30" viewBox="0 0 24 32"><path d="M12 0a11 11 0 0 0-11 11c0 8 11 21 11 21s11-13 11-21A11 11 0 0 0 12 0z" fill="#e0463a"/><circle cx="12" cy="11" r="4" fill="#fff"/></svg>
    </div>
  </div>
  <div class="footer-bar">
    <span>© 2025 | Everstead Roofing. All Rights Reserved.</span>
    <span class="legal"><span>Privacy Policy</span><span>Terms &amp; Conditions</span></span>
    <svg class="to-top" width="14" height="14" viewBox="0 0 14 14"><path d="M2 10l5-6 5 6" fill="none" stroke="#2aa4e2" stroke-width="2"/></svg>
  </div>
</footer>

</body>
</html>
```